Dentistry Office

We want a new design for a Dentist's office website.

The theme is: "We provide high quality, state-of-the-art, dental care in a comfortable, caring environment."

The site currently has a menu on the left of the page with about 40 items on it. There is a great deal of textual content on each page, plus several illustrations.

We want to do this using CSS, so we need specifications in the CSS for all possible elements. The CSS needs to be named in a logical manner for easy use.

Every dentist on the planet seems to use lots of Flash. We don't want to because it is so distracting. We are looking for an elegant solution targeting 24-55 age group, but not excluding anyone.

The following (from another dentist's site) can give you a taste of what we want to communicate on the site:

"After 20 years of teaching dentists how to refine their technique and many years of writing textbooks, I currently devote my time to my office and the hands-on practice of dentistry. I'd like to welcome you personally to my dental practice, and I invite you to meet my highly experienced team of professionals.

"We have offered complete dental care of the highest quality since 1978. We provide Preventive Services, Tooth Whitening and Cosmetic Dentistry for a beautiful smile, Endodontics (root canal treatment) to treat painful teeth, Sedation Dentistry so you can relax, and Dental Implants to restore what is missing. We offer total care.

"Our approach to your health is simple: We use our education, experience and dedication to provide every patient with superior dental care.

"This passion for excellence is not just a goal, but a standard every member of our team holds.

"We also pride ourselves with our state of the art procedures, training and technology. This includes creating a beautiful smile using techniques that preserve as much of the original tooth as possible.

"Our abilities are renowned throughout the dental profession and I hope if you have any questions you will contact us by an e-mail note, by phone or just by dropping by."

Keep in mind the screen shape and dimensions. Your design needs to work in the normal screen proportions, regardless of how it looks when you post it here. Scrolling is OK, but the first impression needs to work.

Keep in mind that there will be about 250 words, or more, on each page.

Competitors web sites:

http://www.brevalkoortho.example/

http://www.quimbelfieldcare.example/

http://www.grinsatdoverellclinic.example/

http://www.trunwickfamilydentalcare.example/

http://www.morvanhaledental.example/

http://www.ubrigandental.example/

We need to compete with these.

Target Market(s)

Generally adults seeking the most experienced and comfortable-to-be-with dentist.

Industry/Entity Type

Training

Requirements
Must have
• Must stand apart from other dentists.
• Must be elegant.
• Must have a horizontal menu structure across all columns, NOT a vertical that requires scrolling, no popout, pop down, etc. menus.
• We are looking for something special.
• Do not waste your time or ours putting up templates and things you have used before.
• Personally, I do not see how someone outside the US can understand the northern California dental market. But you are welcome to try.
Should not have
• Flash or graphics that move
• The look of a template
• Folksy fonts
• Looks like you used it 20 times before

```html
<!DOCTYPE html>
<html lang="en">
<head>
<meta charset="utf-8">
<title>Santa Rosa Dentist – Corwin Haldane, DDS</title>
<link rel="stylesheet" href="https://fonts.googleapis.com/css2?family=Arimo:ital,wght@0,400;0,700;1,700&family=Questrial&display=swap">
<style>
:root{
  --page-bg:#2b2b2b;
  --band-bg:#333333;
  --black:#000000;
  --nav-text:#d4d4d4;
  --nav-divider:#555555;
  --accent-blue:#3aa6e0;
  --link-blue:#2a8fd4;
  --panel-grey:#e4e4e6;
  --panel-blue:#27a4e3;
  --intro-navy:#22228a;
  --body-text:#e8e8e8;
  --muted-text:#bdbdbd;
  --rule:#5a5a5a;
  --tab-education:#1f1f78;
  --tab-preventive:#2b2b9c;
  --tab-cosmetics:#1565b9;
  --tab-restorations:#35a9e4;
  --tab-visiting:#17b38e;
}
*{margin:0;padding:0;box-sizing:border-box}
html,body{width:810px;height:1200px;overflow:hidden;background:var(--page-bg)}
body{font-family:"Arimo",Arial,sans-serif;color:var(--body-text);position:relative}
a{color:inherit;text-decoration:none}

.site-nav{position:absolute;left:33px;top:4px;width:738px;height:28px;background:linear-gradient(#2a2a2a,#141414);display:flex}
.site-nav a{font-size:12px;font-weight:700;color:var(--nav-text);line-height:28px;padding-left:19px;border-right:1px solid var(--nav-divider)}
.site-nav a:last-child{border-right:none}

.site-header{position:absolute;left:33px;top:32px;width:738px;height:88px;background:var(--band-bg);padding:16px 0 0 18px}
.site-title{font-size:16.5px;font-weight:700;color:var(--accent-blue);line-height:20px;letter-spacing:-0.1px}
.site-address{font-size:10.5px;color:#d0d0d0;margin-top:1px}

.hero{position:absolute;left:33px;top:120px;width:738px;height:292px;display:flex}
.hero-intro{width:252px;background:var(--panel-grey);position:relative;padding:62px 18px 0 19px;font-family:"Questrial",Arial,sans-serif;font-size:13.4px;line-height:17.2px;color:var(--intro-navy)}
.hero-branch{position:absolute;left:0;bottom:0;width:252px;height:120px;background:linear-gradient(160deg,rgba(228,228,230,0) 30%,#a9a0a6 75%,#6b6166)}
.hero-award{width:254px;background:var(--panel-blue);margin-left:1px;padding:62px 14px 0 16px;font-family:"Questrial",Arial,sans-serif;font-size:13.4px;line-height:17.2px;color:#fff}
.hero-photo{flex:1;margin-left:2px;background:linear-gradient(120deg,#d9d7cf,#e8e6df 45%,#c9c3b4 75%,#b8b6a8)}

.treatment-menu{position:absolute;left:33px;top:412px;width:738px;height:212px;background:var(--black)}
.menu-column{position:absolute;top:22px;width:140px}
.menu-tab{display:block;width:122px;height:28px;border-radius:2px;font-size:13.6px;font-weight:700;font-style:italic;color:#fff;line-height:28px;text-align:center;box-shadow:inset 0 0 0 1px rgba(255,255,255,.18)}
.menu-links{list-style:none;margin-top:9px}
.menu-links li{font-size:9px;font-weight:700;font-style:italic;color:#fff;line-height:14.2px;padding-left:1px}
.col-education{left:20px}.col-education .menu-tab{background:var(--tab-education)}
.col-preventive{left:161px}.col-preventive .menu-tab{background:var(--tab-preventive)}
.col-cosmetics{left:307px}.col-cosmetics .menu-tab{background:var(--tab-cosmetics)}
.col-restorations{left:453px}.col-restorations .menu-tab{background:var(--tab-restorations)}
.col-visiting{left:600px}.col-visiting .menu-tab{background:var(--tab-visiting);text-align:left;padding-left:2px}

.column-divider{position:absolute;left:322px;top:624px;width:1px;height:570px;background:var(--rule)}
.footer-rule{position:absolute;left:33px;top:1082px;width:736px;height:1px;background:var(--rule)}

.section-heading{font-size:16.4px;font-weight:700;color:var(--accent-blue);line-height:20px}
.services{position:absolute;left:53px;top:644px;width:262px}
.services p{font-size:10.5px;line-height:14.2px;margin-top:14px}
.services .services-heading{margin-bottom:4px}
.underline{text-decoration:underline}

.commitment{position:absolute;left:340px;top:645px;width:430px}
.commitment p{font-size:10.5px;line-height:13.5px;margin-top:12.5px}
.commitment .section-heading{margin-bottom:5px}
.signature{font-size:16.4px;font-weight:700;color:var(--accent-blue);margin-top:9px}

.footer-links{position:absolute;left:53px;top:1094px}
.footer-links a{display:block;font-size:10.5px;font-weight:700;color:var(--link-blue);line-height:13px;margin-bottom:14px}
.footer-offer{position:absolute;left:340px;top:1096px;width:430px;color:var(--muted-text)}
.footer-offer p{font-size:10.5px;line-height:13px}
.footer-offer .fine-print{font-size:7px;line-height:9px}
.footer-offer .contact{margin-top:17px}
</style>
</head>
<body>

<nav class="site-nav">
  <a href="#" style="width:131px">Home page</a>
  <a href="#" style="width:148px">Why we are different</a>
  <a href="#" style="width:150px">Technologies we offer</a>
  <a href="#" style="width:128px">Meet Dr. Haldane</a>
  <a href="#" style="width:82px">Our Staff</a>
  <a href="#" style="flex:1">Contact us/Links</a>
</nav>

<header class="site-header">
  <h1 class="site-title">Santa Rosa Dentist - Corwin Haldane, DDS, Providing Cosmetic Dentistry Excellence to Patients in Santa Rosa, Sonoma County and the San Francisco Bay Area.</h1>
  <p class="site-address">Located at 2240 Larkfield Way, Ste B-3, Santa Rosa, CA 95405</p>
</header>

<section class="hero">
  <div class="hero-intro">
    <p>In Santa Rosa, when you’re a patient of Dr. Haldane, you can be confident that you’re receiving care from the most experienced, knowledgeable, and skilled cosmetic dentist in Sonoma County.</p>
    <div class="hero-branch" role="img" aria-label="Illustration of a blossoming branch"></div>
  </div>
  <div class="hero-award">
    <p>Dr. Haldane is an award-winning leader in restorative dentistry and a genial professional. His humor, dedication, and talent ensure you a pleasant experience and superb, long-lasting results.</p>
  </div>
  <div class="hero-photo" role="img" aria-label="Photo of a smiling patient"></div>
</section>

<section class="treatment-menu">
  <div class="menu-column col-education">
    <a class="menu-tab" href="#">Education</a>
    <ul class="menu-links">
      <li>Emergency Dental Care</li><li>Your Mouth</li><li>Your Tooth</li><li>Cracked Tooth?</li><li>Missing a Tooth?</li><li>Sensitive Teeth</li><li>Dry Mouth</li><li>Tooth Grinding</li><li>Sleep Dentistry</li><li>Videos</li>
    </ul>
  </div>
  <div class="menu-column col-preventive">
    <a class="menu-tab" href="#">Preventative</a>
    <ul class="menu-links">
      <li>What is Preventive Care?</li><li>Taking Care of Your Teeth</li><li>Eating Right</li><li>Dental Check-Ups</li><li>Sealants</li><li>Periodontal Disease</li><li>Kicking the Habit</li><li>Night Guards</li><li>Dental X-Rays</li><li>Antibiotics with Treatment</li>
    </ul>
  </div>
  <div class="menu-column col-cosmetics">
    <a class="menu-tab" href="#">Cosmetics</a>
    <ul class="menu-links">
      <li>Cosmetic Dentistry</li><li>Bleaching and Whitening</li><li>Cosmetic Bonding</li><li>Esthetic Veneers</li><li>Tooth Shaping</li>
    </ul>
  </div>
  <div class="menu-column col-restorations">
    <a class="menu-tab" href="#">Restorations</a>
    <ul class="menu-links">
      <li>Crowns/Caps: Each Step</li><li>CMBRs</li><li>Porcelain Bridges</li><li>Bonded Dental Bridges</li><li>Gold Restorations</li><li>Implants</li><li>Treating Cracked Teeth</li><li>Periodontal (gum) Treatment</li>
    </ul>
  </div>
  <div class="menu-column col-visiting">
    <a class="menu-tab" href="#">Visiting our office</a>
    <ul class="menu-links">
      <li>Where to Stay</li><li>First Visit | Map</li><li>Financial Policy</li><li>Dental Insurance</li>
    </ul>
  </div>
</section>

<div class="column-divider"></div>
<div class="footer-rule"></div>

<section class="services">
  <h2 class="section-heading services-heading">Dr. Haldane Provides</h2>
  <p>General dentistry—oral hygiene, cavity detection and repair, crowns.</p>
  <p>Cosmetic/restorative dentistry—broken or misshapen teeth, crooked smiles, unsightly gaps.</p>
  <p><span class="underline">Non-metal fillings</span>—nontoxic, durable tooth-colored resin fillings that are proven to provide better results.</p>
  <p>Tooth shaping—extending, shortening or otherwise reshaping teeth for improved esthetics.</p>
  <p>Complete smile make-over’s—resin veneers that reshape the whole mouth while preserving natural teeth.</p>
  <p>Tooth whitening—at-home bleaching options to make teeth appear years younger.<br>Laser Dentistry, Sleep Dentistry, and Implant Dentistry with the Finest and Latest Equipment and Materials.</p>
  <p>Dental Implants to replace missing teeth.<br>Sedation Dentistry so you can be relaxed.</p>
</section>

<section class="commitment">
  <h2 class="section-heading">Dr. Haldane’ Commitment</h2>
  <p>After 25 years of teaching dentists how to refine their technique and many years of writing textbooks, I currently devote my time to my office and the hands-on practice of dentistry. I’d like to welcome you personally to my dental practice, and I invite you to meet my highly experienced team of professionals.</p>
  <p>Dr. Haldane and his Associated have offered complete dental care of the highest quality since 1978. We provide Preventive Services, Tooth Whitening and Cosmetic Dentistry for a beautiful smile, Endodontics (root canal treatment) to treat painful teeth, Sedation Dentistry so you can relax, and Dental Implants to restore what is missing. We offer total care.</p>
  <p>Our approach to your health is simple: We use our education, experience and dedication to provide every patient with superior dental care.</p>
  <p>This passion for excellence is not just a goal, but a standard every member of our team holds.</p>
  <p>We also pride ourselves with our state of the art procedures, training and technology. This includes creating a beautiful smile using techniques that preserve as much of the original tooth as possible.</p>
  <p>Our abilities are renowned throughout the dental profession and I hope if you have any questions you will contact us by an e-mail note, by phone or just by dropping by.</p>
  <p>Thank you.</p>
  <p>Sincerely,</p>
  <p class="signature">Corwin Haldane, DDS FAGD</p>
</section>

<nav class="footer-links">
  <a href="#">Office Hours and Map to Office</a>
  <a href="#">Where to stay?</a>
</nav>

<section class="footer-offer">
  <p>We offer an Initial Patient Examination, X-rays and Cleaning for $79.00.</p>
  <p class="fine-print">**New patients only. Offers are cash patients only.  Insurance will be billed at full value.</p>
  <p class="contact">Please contact us at (707) 555-0142.</p>
  <p class="contact">To contact us outside office hours for an emergency, please call (707) 555-0187.</p>
</section>

</body>
</html>
```